I need a website built for my organization.
We are the world's largest network of music producers.
The website should be professional, sharp, and high quality., We need a website built for The Halvern Sound Guild. We are one of the World's largest association of music producers.
The site must be professional, sharp, and high quality., I need a website built for my organization.
The site must be professional, sharp, and high quality.
Somewhere in the top half of the site there should be a form for the user to fill out. The details of the form are as follows:
Title (large and bold): Contact Us or Submit Your Music
Fields to include (* = required): First Name*, Last Name*, Age, Zip Code, Email Address*, Daytime Phone, Evening Phone, Comments
Then, there will be a "submit" button to proceed to next step of form. Just below the "submit" button, should be the following verbiage: "After submitting, you will have the opportunity to upload demos of your music (optional) and provide other pertinent information about yourself, band, or group."
Target Market(s)
Music producers and aspiring musicians
Industry/Entity Type
Group
Colors
Designer to choose colors to be used in the design.
Look and feel

```html
<!DOCTYPE html>
<html lang="en">
<head>
<meta charset="utf-8">
<title>The Halvern Sound Guild</title>
<link href="https://fonts.googleapis.com/css2?family=Open+Sans:wght@300;400;600;700&display=swap" rel="stylesheet">
<style>
  :root{
    --paper:#f4f2ee;
    --plum:#5e1a4f;
    --plum-deep:#2a0f24;
    --gold:#f5b800;
    --orange:#f08c00;
    --red:#c0281c;
    --ink:#3a3a3a;
    --muted:#666;
    --line:#d6d3cc;
    --panel:#ffffff;
    --panel-mid:#efeeeb;
    --foot:#1f2024;
    --foot-bar:#0c0c0d;
    --foot-text:#b9b9b9;
    --foot-field:#5a5b5f;
  }
  *{box-sizing:border-box;margin:0;padding:0}
  html,body{width:796px;height:1200px;overflow:hidden}
  body{position:relative;background:var(--paper);font-family:"Open Sans",Arial,sans-serif;color:var(--ink)}
  .abs{position:absolute}

  /* header */
  .site-header{left:0;top:0;width:796px;height:64px;border-top:3px solid var(--plum);background:var(--paper)}
  .brand{left:40px;top:18px;display:flex;align-items:center;gap:7px;font-size:13px;font-weight:600;color:#333}
  .brand-square{width:14px;height:14px;background:#333}
  .main-nav{left:268px;top:20px;display:flex;font-size:9px;text-transform:uppercase;color:#333}
  .main-nav a{display:block;height:22px;line-height:22px;padding:0 10px;color:inherit;text-decoration:none;margin-right:var(--gap,21px)}
  .main-nav a.active{background:var(--gold);color:#fff}

  /* hero */
  .hero{left:0;top:64px;width:796px;height:276px;background:radial-gradient(ellipse at center,#3d1836 0%,var(--plum-deep) 70%)}
  .hero-frame{left:44px;top:12px;width:709px;height:251px;border:3px solid var(--plum);overflow:hidden}
  .hero-photo{position:absolute;inset:0;background:linear-gradient(180deg,#2a3a52 0%,#6b5a3a 35%,#8a6f3e 55%,#2b2420 100%)}
  .hero-band{position:absolute;left:0;right:0;bottom:0;height:82px;background:rgba(0,0,0,.55)}
  .hero-copy{position:absolute;left:0;right:0;top:166px;text-align:center}
  .hero-copy .lead{font-weight:300;font-size:22px;color:#fff;line-height:26px}
  .hero-copy .accent{font-weight:700;font-size:22px;color:var(--orange);line-height:28px}
  .hero-copy .cta{display:inline-block;font-size:9px;line-height:14px;font-weight:700;color:var(--red);text-decoration:underline}
  .hero-shadow{top:340px;width:120px;height:10px;background:radial-gradient(ellipse at top,rgba(0,0,0,.25),transparent 70%)}

  /* welcome */
  .welcome-title{left:40px;top:356px;width:716px;display:flex;align-items:center;gap:14px;font-size:22px;font-weight:300;color:#444}
  .welcome-title::before,.welcome-title::after{content:"";flex:1;height:1px;background:#aaa}
  .welcome-text{left:133px;top:398px;width:530px;font-size:9.5px;line-height:14.5px;text-align:center;color:#444}

  /* three columns */
  .info-panel{left:40px;top:483px;width:716px;height:208px;background:var(--panel);border:1px solid var(--line);display:flex}
  .info-col{position:relative;width:235px;padding:10px 24px}
  .info-col.middle{width:244px;background:var(--panel-mid)}
  .info-col h2{font-size:17px;font-weight:400;color:#444;margin:3px 0 14px}
  .news-item{margin-bottom:14px;font-size:9px;line-height:14px}
  .news-item a{color:#333;text-decoration:underline}
  .news-item .date{display:block;color:var(--red)}
  .more-link{position:absolute;right:14px;bottom:6px;font-size:9px;font-weight:700;color:var(--plum);text-decoration:underline}
  .newsletter p{font-size:9px;line-height:15px;color:#555;margin-bottom:12px}
  .newsletter-form{display:flex}
  .newsletter-form span{width:135px;height:24px;background:#fff;font-size:9px;font-style:italic;color:#777;line-height:24px;padding-left:11px}
  .newsletter-form b{width:51px;height:24px;background:var(--plum);color:#fff;font-size:11px;line-height:24px;text-align:center}

  /* submit form */
  .form-title{left:60px;top:705px;font-size:14px;font-weight:700;color:#333;letter-spacing:.3px}
  .field{width:308px;height:25px;background:#fff;border:1px solid #bbb;font-size:9.5px;line-height:13px;color:#333;padding:5px 10px}
  .field.tall{height:104px}
  .req{color:var(--red)}
  .submit-btn{left:644px;top:935px;width:75px;height:28px;background:var(--plum);color:#fff;font-size:11px;font-weight:700;text-align:center;line-height:28px;border-bottom:2px solid #3a0e31}
  .submit-note{left:319px;top:966px;width:400px;font-size:7.5px;line-height:10px;color:var(--muted);text-align:right}

  /* footer */
  .site-footer{left:0;top:991px;width:796px;height:180px;background:var(--foot);border-top:3px solid var(--plum);color:var(--foot-text)}
  .foot-col{top:14px}
  .foot-col h3{font-size:15px;font-weight:400;color:#ddd;margin-bottom:12px}
  .foot-col ul{list-style:none;font-size:9px;line-height:14.6px}
  .foot-col p{font-size:8px;line-height:13px;color:#999}
  .foot-field{width:174px;height:21px;background:var(--foot-field);font-size:8px;color:#bbb;padding:4px 8px;margin-bottom:7px}
  .foot-field.tall{height:41px}
  .foot-send{left:701px;top:153px;width:54px;height:19px;background:var(--foot-field);font-size:8px;color:#ddd;text-align:center;line-height:19px}
  .foot-bar{left:0;top:1171px;width:796px;height:29px;background:var(--foot-bar);font-size:8px;color:#777;padding:9px 0 0 65px}
</style>
</head>
<body>

<header class="site-header abs">
  <div class="brand abs"><span class="brand-square"></span>The Halvern Sound Guild</div>
  <nav class="main-nav abs">
    <a class="active" href="#">Home</a>
    <a href="#" style="--gap:19px">About</a>
    <a href="#" style="--gap:29px">News</a>
    <a href="#" style="--gap:21px">Membership</a>
    <a href="#" style="--gap:19px">Events</a>
    <a href="#" style="--gap:23px">Resources</a>
    <a href="#">Contact</a>
  </nav>
</header>

<section class="hero abs">
  <div class="hero-frame abs">
    <div class="hero-photo" role="img" aria-label="Producer at a mixing desk facing an orchestra in a recording studio"></div>
    <div class="hero-band"></div>
    <div class="hero-copy">
      <div class="lead">The World's Largest Network of</div>
      <div class="accent">Music Producers</div>
      <a class="cta" href="#">Join Now</a>
    </div>
  </div>
</section>
<div class="hero-shadow abs" style="left:30px"></div>
<div class="hero-shadow abs" style="left:646px"></div>

<h1 class="welcome-title abs">Welcome to Our Site</h1>
<p class="welcome-text abs">Lorem ipsum is simply dummy text of the printing and typesetting industry. Lorem Ipsum has been the industry's standard dummy text ever since the 1500s, when an unknown printer took a galley of type and scrambled it to make a type specimen book. It has survived not only five centuries, but also the leap into electronic typesetting, remaining essentially unchanged. It was popularised in the 1960s with the release of Letraset sheets containing Lorem Ipsum passages.</p>

<section class="info-panel abs">
  <div class="info-col">
    <h2>Latest News</h2>
    <div class="news-item"><a href="#">Verano PE Evaporator: The Clever Way to Evaporation in Sample Vials</a><span class="date">12.02.2013</span></div>
    <div class="news-item"><a href="#">FISH: Fluorescence In Situ Hybridisation</a><span class="date">14.12.2012</span></div>
    <div class="news-item"><a href="#">Live Cell Printing for High Content Analysis and Cell Assays</a><span class="date">26.03.2012</span></div>
    <a class="more-link" href="#">more news</a>
  </div>
  <div class="info-col middle newsletter">
    <h2>News letter</h2>
    <p>If you'd like to receive the latest news and other information, type in your email address below and then click "GO" button.</p>
    <div class="newsletter-form"><span>Enter your email here</span><b>GO</b></div>
  </div>
  <div class="info-col">
    <h2>Latest Events</h2>
    <div class="news-item"><a href="#">Verano PE Evaporator: The Clever Way to Evaporation in Sample Vials</a><span class="date">12.02.2013</span></div>
    <div class="news-item"><a href="#">FISH: Fluorescence In Situ Hybridisation</a><span class="date">14.12.2012</span></div>
    <div class="news-item"><a href="#">Live Cell Printing for High Content Analysis and Cell Assays</a><span class="date">26.03.2012</span></div>
    <a class="more-link" href="#">more Events</a>
  </div>
</section>

<h2 class="form-title abs">SUBMIT YOUR MUSIC</h2>
<div class="field abs" style="left:57px;top:741px">First Name<span class="req">*</span></div>
<div class="field abs" style="left:57px;top:782px">Last Name<span class="req">*</span></div>
<div class="field abs" style="left:57px;top:823px">Age</div>
<div class="field abs" style="left:57px;top:864px">Zip Code</div>
<div class="field abs" style="left:57px;top:904px">Email Address<span class="req">*</span></div>
<div class="field abs" style="left:411px;top:741px">Daytime Phone</div>
<div class="field abs" style="left:411px;top:782px">Evenig Time Phone</div>
<div class="field tall abs" style="left:411px;top:823px">Comments</div>
<div class="submit-btn abs">SUBMIT</div>
<p class="submit-note abs">After submitting, you will have the opportunity to upload demos of your music (optional) and provide other pertinent information about yourself, band, or group.</p>

<footer class="site-footer abs">
  <div class="foot-col abs" style="left:53px">
    <h3>Quick LInks</h3>
    <ul><li>Home</li><li>Services</li><li>Case studies</li><li>Engaging us</li><li>About</li><li>Conflict resolution</li><li>About</li><li>Contact</li></ul>
  </div>
  <div class="foot-col abs" style="left:201px">
    <h3>Quick LInks</h3>
    <ul><li>Home</li><li>Services</li><li>Case studies</li><li>Engaging us</li><li>About</li><li>Conflict resolution</li><li>About</li><li>Contact</li></ul>
  </div>
  <div class="foot-col abs" style="left:367px;width:150px">
    <h3>Quick Contact</h3>
    <p>It has survived not only five centuries, but also the leap into electronic typesetting, remaining essentially unchanged. It was popularised in the 1960s</p>
    <p style="margin-top:10px">Mob : 000 00000<br>Email: info@halvernsound.org</p>
  </div>
  <div class="foot-col abs" style="left:581px">
    <h3>Send a Message</h3>
    <div class="foot-field">Name</div>
    <div class="foot-field">Email</div>
    <div class="foot-field tall">Message</div>
  </div>
  <div class="foot-send abs">SUBMIT</div>
</footer>
<div class="foot-bar abs">Copyright © 2013 Halvern Sound Guild</div>

</body>
</html>
```